Quillmere Voyage Care Web Page

To create a web page that has the number 1 goal of converting Zorvix Ad / Trellisgram Ads clicks into paying customers.
The site will feed into a web application where travellers can enter their trip and purchase a Voyawell Ready Pack.
The page / site needs to be able to tell people what we do and encourage them to start the process of getting a Voyawell Ready Pack.
It should be a wordpress theme.
Please see the attached brief for more information.

```html
<!DOCTYPE html>
<html lang="en">
<head>
<meta charset="utf-8">
<title>Quillmere Voyage Care</title>
<link href="https://fonts.googleapis.com/css2?family=Outfit:wght@500;600;700&family=Roboto:wght@400;500;700&display=swap" rel="stylesheet">
<style>
:root{
  --navy:#1b3863;
  --navy-deep:#162f55;
  --sky:#3bb3da;
  --teal:#1f6e96;
  --ink:#1d2b3f;
  --muted:#5b6472;
  --pale:#f1f1f1;
  --white:#ffffff;
}
*{margin:0;padding:0;box-sizing:border-box}
html,body{width:1200px;height:4096px;overflow:hidden}
body{font-family:"Roboto",Arial,sans-serif;color:var(--ink);background:var(--white);position:relative}
.abs{position:absolute}
h1,h2,h3,.heading{font-family:"Outfit",Arial,sans-serif;color:var(--navy);font-weight:600}
a{text-decoration:none;color:inherit}
.btn{position:absolute;display:flex;align-items:center;justify-content:center;background:var(--teal);color:#fff;font-family:"Roboto",sans-serif;font-weight:700;font-size:14px;border-radius:4px}
.photo{position:absolute;border-radius:2px}

/* top bar */
.topbar{position:absolute;left:0;top:0;width:1200px;height:40px;background:var(--sky);color:#fff;font-size:12.5px;font-weight:500}
.topbar span{position:absolute;top:12px;display:flex;align-items:center;gap:10px}
.nav{position:absolute;left:0;top:40px;width:1200px;height:71px;background:var(--navy)}
.brand{position:absolute;display:flex;align-items:center;gap:10px;color:#fff;font-family:"Outfit",sans-serif;font-weight:600;font-size:17px}
.brand i{display:block;width:34px;height:34px;border-radius:50%;background:var(--sky)}
.nav ul{position:absolute;left:422px;top:27px;list-style:none;display:flex;gap:0;color:#fff;font-size:12.5px;font-weight:500}
.nav li{margin-right:38px}

/* hero */
.hero{position:absolute;left:0;top:111px;width:1200px;height:556px;overflow:hidden;background:linear-gradient(100deg,#3e3a35 0%,#6f6456 35%,#b9ad9c 60%,#8a8178 100%)}
.hero h1{position:absolute;left:113px;top:126px;color:#fff;font-size:55px;line-height:58px;font-weight:600}
.hero p{position:absolute;left:113px;top:264px;width:500px;color:#fff;font-size:11.5px;line-height:19px;font-weight:500}
.quote-box{position:absolute;left:113px;top:327px;width:495px;height:53px;background:#fff;border-radius:3px}
.quote-box .label{position:absolute;left:80px;top:19px;font-size:11.5px;font-weight:500;color:var(--ink)}
.quote-box .go{position:absolute;left:383px;top:6px;width:105px;height:41px;background:var(--sky);color:#fff;font-size:11.5px;font-weight:700;display:flex;align-items:center;justify-content:center;border-radius:3px}

/* partners */
.partner{position:absolute;top:722px;height:40px;background:#d6d9de;border-radius:6px}

/* about */
.about h2{position:absolute;left:664px;top:848px;width:420px;font-size:38px;line-height:45px}
.body-copy{position:absolute;font-size:11px;line-height:19px;color:var(--muted)}

.section-title{position:absolute;left:0;width:1200px;text-align:center;font-size:39px}
.lead{position:absolute;left:320px;width:560px;text-align:center;font-size:11px;line-height:19px;color:var(--muted)}

.list{position:absolute;list-style:none;font-size:11px;color:var(--muted)}
.list li{position:relative;padding-left:26px;height:22.5px}
.list li::before{content:"";position:absolute;left:0;top:4px;width:7px;height:7px;border-radius:50%;background:var(--sky)}
.sub{position:absolute;font-size:22px;font-weight:600}
.smallhead{position:absolute;font-size:10.5px;line-height:15px;font-weight:700;color:var(--navy)}

.grey-band{position:absolute;left:0;top:1816px;width:1200px;height:436px;background:var(--pale);overflow:hidden}

/* how it works */
.step{position:absolute;top:2390px;width:260px;text-align:center}
.step .num{position:absolute;font-family:"Outfit",sans-serif;font-weight:600;font-size:22px;color:var(--navy);top:0}
.step .ring{margin:0 auto;width:95px;height:95px;border-radius:50%;background:var(--sky);border:4px solid #cfeef8;box-shadow:0 0 0 2px var(--sky);display:flex;align-items:center;justify-content:center}
.step .cap{margin-top:30px;font-size:14px;font-weight:700;color:var(--navy);line-height:22px}

/* testimonials */
.testi{position:absolute;left:0;top:2719px;width:1200px;height:408px;background:var(--navy)}
.testi h2{position:absolute;left:0;top:56px;width:1200px;text-align:center;color:#fff;font-size:39px}
.card{position:absolute;top:125px;width:425px;height:228px;background:#fff;border-radius:2px}
.avatar{position:absolute;left:38px;top:34px;width:60px;height:60px;border-radius:50%;background:linear-gradient(135deg,#c9ccd2,#7d8591)}
.card .name{position:absolute;left:120px;top:40px;font-size:15px;font-weight:700;color:var(--ink)}
.card .role{position:absolute;left:120px;top:66px;font-size:10px;color:var(--muted)}
.card .stars{position:absolute;left:120px;top:86px;color:#f6b800;font-size:16px;letter-spacing:2px}
.card .quote{position:absolute;left:48px;top:134px;width:345px;font-size:10px;line-height:19px;color:var(--muted)}
.card .qm{position:absolute;font-family:Georgia,serif;font-size:40px;color:#dfe3e8}
.arrow{position:absolute;width:36px;height:36px;border:1.5px solid #fff;border-radius:50%}

/* blog */
.post{position:absolute;top:3253px;width:283px;height:338px;background:#fff;box-shadow:0 4px 18px rgba(0,0,0,.07)}
.post .img{height:175px}
.post .date{position:absolute;left:24px;top:204px;font-size:10.5px;font-weight:500;color:var(--ink)}
.post h3{position:absolute;left:24px;top:236px;width:230px;font-family:"Roboto",sans-serif;font-size:14px;line-height:22px;font-weight:700;color:var(--navy)}
.post .more{position:absolute;left:24px;top:296px;font-size:11px;font-weight:500;color:var(--sky)}

/* cta */
.cta{position:absolute;left:0;top:3648px;width:1200px;height:248px;background:var(--sky);overflow:hidden}
.cta h2{position:absolute;left:0;top:52px;width:1200px;text-align:center;color:#fff;font-size:39px}
.cta p{position:absolute;left:320px;top:110px;width:560px;text-align:center;color:#fff;font-size:11px;line-height:18px}

/* footer */
.footer{position:absolute;left:0;top:3896px;width:1200px;height:200px;background:var(--navy);color:#fff}
.fcol{position:absolute;top:42px;font-size:9.5px;line-height:17px}
.fcol h4{font-family:"Roboto",sans-serif;font-size:13.5px;font-weight:700;margin-bottom:14px}
</style>
</head>
<body>

<header>
  <div class="topbar">
    <span style="left:112px">
      <svg width="15" height="15" viewBox="0 0 24 24" fill="#fff"><path d="M6.6 10.8a15.1 15.1 0 0 0 6.6 6.6l2.2-2.2c.3-.3.7-.4 1-.2 1.1.4 2.3.6 3.6.6.6 0 1 .4 1 1V20c0 .6-.4 1-1 1C10.6 21 3 13.4 3 4c0-.6.4-1 1-1h3.5c.6 0 1 .4 1 1 0 1.3.2 2.5.6 3.6.1.3 0 .7-.2 1z"/></svg>
      0915 302 8841
    </span>
    <span style="left:265px">
      <svg width="16" height="12" viewBox="0 0 16 12" fill="#fff"><path d="M0 0h16v12H0z" opacity=".95"/><path d="M0 0l8 6 8-6" stroke="#3bb3da" stroke-width="1.4" fill="none"/></svg>
      info@quillmerevoyage.com
    </span>
  </div>
  <nav class="nav">
    <div class="brand" style="left:112px;top:17px"><i></i>Quillmere Voyage Care</div>
    <ul>
      <li>Individual/Family</li><li>Small Buisness</li><li>Senior</li><li>Disease</li><li>Country</li><li>Contact Us</li><li>About Us</li>
    </ul>
  </nav>
</header>

<section class="hero">
  <div class="abs" role="img" aria-label="Smiling couple at a laptop holding a payment card" style="left:480px;top:0;width:720px;height:556px;background:linear-gradient(90deg,rgba(0,0,0,0),rgba(200,190,175,.35))"></div>
  <h1>Welcome to Quillmere<br>Voyage Care</h1>
  <p>We listen to you, discover the root cause of your ailment, and create a treatment program tailored for your unique needs to live pain-free and well.</p>
  <div class="quote-box">
    <svg class="abs" style="left:36px;top:15px" width="28" height="22" viewBox="0 0 28 22" fill="#1b3863"><circle cx="14" cy="6" r="5"/><circle cx="5" cy="8" r="3.5"/><circle cx="23" cy="8" r="3.5"/><path d="M5 22c0-6 4-9 9-9s9 3 9 9z"/><path d="M0 20c0-4 2-6 5-6s4 1 4 2v4zM28 20c0-4-2-6-5-6s-4 1-4 2v4z"/></svg>
    <span class="label">For Individual/Family</span>
    <svg class="abs" style="left:349px;top:22px" width="13" height="8" viewBox="0 0 13 8"><path d="M0 0h13L6.5 8z" fill="#1b3863"/></svg>
    <span class="go">QUOTE NOW</span>
  </div>
  <svg class="abs" style="left:588px;top:483px" width="24" height="30" viewBox="0 0 24 30"><rect x="1" y="1" width="22" height="28" rx="11" fill="none" stroke="#fff" stroke-width="2"/><path d="M8 13l4 4 4-4" stroke="#fff" stroke-width="2" fill="none"/></svg>
  <svg class="abs" style="left:0;top:500px" width="1200" height="56" viewBox="0 0 1200 56"><path d="M0 56V56C400 56 800 40 1200 28V56Z" fill="#3bb3da"/><path d="M0 56C450 55 850 48 1200 38V56Z" fill="#fff"/></svg>
</section>

<section class="partners" aria-label="Partners">
  <div class="partner" style="left:160px;width:130px"></div>
  <div class="partner" style="left:355px;width:115px"></div>
  <div class="partner" style="left:542px;width:145px"></div>
  <div class="partner" style="left:764px;width:142px"></div>
  <div class="partner" style="left:974px;width:66px"></div>
</section>

<section class="about">
  <div class="photo" role="img" aria-label="Doctor in a mask consulting an elderly patient and his daughter" style="left:113px;top:847px;width:495px;height:350px;background:linear-gradient(120deg,#e8ecef,#c7cfd6 50%,#8fa0b0)"></div>
  <svg class="abs" style="left:538px;top:1127px" width="70" height="70" viewBox="0 0 70 70"><path d="M70 0V70H0z" fill="#3bb3da"/><circle cx="50" cy="48" r="8" fill="#fff"/></svg>
  <h2>About Quillmere Voyage Care</h2>
  <p class="body-copy" style="left:664px;top:950px;width:375px">Quillmere is the healthcare division of Vextral Labs – a third-generation software provider and Software as a Service (SAAS) company committed to developing a tailored experience for all stakeholders within the data-for-health world.</p>
  <p class="body-copy" style="left:664px;top:1044px;width:375px">The company was founded in 2021 by Oren Castell and Milo Brenner, on the basis of two previously successful collaborations over the past decade. Its reputation also rests on the relationships previously built with leading laboratories and clinics, as well as individuals within the National Care Service and Government.</p>
  <a class="btn" style="left:665px;top:1154px;width:126px;height:43px">Read More</a>
</section>

<section class="services">
  <h2 class="section-title" style="top:1250px">Our Services &amp; Products</h2>
  <p class="lead" style="top:1308px">Each one of us is different and we each need a unique approach to achieve health and wellness. We offer a wide-range of evidence-based rehabilitation.</p>

  <h3 class="sub" style="left:113px;top:1418px">Treatment Services</h3>
  <ul class="list" style="left:113px;top:1470px"><li>Walk-in clinic</li><li>Family Medicine</li><li>Travel Medicine</li><li>Cosmetic Medicine</li></ul>
  <ul class="list" style="left:342px;top:1470px"><li>Shockwave Therapy</li><li>Massage Therapy</li><li>Laser Therapy</li><li>Naturopathic Medicine</li></ul>
  <p class="smallhead" style="left:113px;top:1584px;width:300px">Learn More About Our Medical, Rehabilitation, Therapy &amp; Wellness Services</p>
  <p class="body-copy" style="left:113px;top:1626px">Find out all the ways we can help you recover and live well.</p>
  <a class="btn" style="left:113px;top:1671px;width:199px;height:43px">Check Out Our Services</a>
  <div class="photo" role="img" aria-label="Nurse checking a resting elderly patient with a stethoscope" style="left:608px;top:1390px;width:479px;height:325px;background:linear-gradient(130deg,#b9a48c,#d9d4cc 45%,#8797a6)"></div>
  <div class="abs" style="left:534px;top:1645px;width:179px;height:116px;background:#fff;box-shadow:0 4px 16px rgba(0,0,0,.1);display:flex;flex-direction:column;align-items:center;justify-content:center;gap:8px">
    <i style="display:block;width:28px;height:28px;border-radius:50%;background:var(--navy)"></i>
    <span style="font-family:Outfit,sans-serif;font-weight:600;font-size:12px;color:var(--navy)">Quillmere Voyage Care</span>
  </div>
</section>

<section class="grey-band">
  <svg class="abs" style="left:1030px;top:250px" width="200" height="220" viewBox="0 0 200 220"><circle cx="70" cy="70" r="65" fill="#e4e4e4"/></svg>
  <div class="photo" role="img" aria-label="Hands fitting a black wrist brace" style="left:113px;top:53px;width:495px;height:324px;background:linear-gradient(120deg,#f2f2f2,#d8d3cf 45%,#a8a39f)"></div>
  <svg class="abs" style="left:538px;top:307px" width="70" height="70" viewBox="0 0 70 70"><path d="M70 0V70H0z" fill="#3bb3da"/><circle cx="50" cy="48" r="8" fill="#fff"/></svg>
  <h3 class="sub" style="left:663px;top:66px">Treatment Products</h3>
  <ul class="list" style="left:663px;top:112px"><li>Sports Medicine</li><li>Physiatrists</li><li>Medical Acupuncture</li><li>Custom Orthotics</li></ul>
  <ul class="list" style="left:895px;top:112px"><li>Nutraceuticals</li><li>Custom Bracing</li><li>Topical Creams</li><li>Compression Stockings</li></ul>
  <p class="smallhead" style="left:663px;top:225px">Learn More About Our Medical &amp; Therapeutic Products</p>
  <p class="body-copy" style="left:663px;top:256px;width:340px">Always top quality and chosen for their effectiveness if treaing your symptoms.</p>
  <a class="btn" style="left:665px;top:318px;width:220px;height:43px">Learn More About Products</a>
</section>

<section class="how">
  <h2 class="section-title" style="top:2294px">How it Works</h2>
  <div class="step" style="left:81px"><span class="num" style="left:69px">1</span><div class="ring"><svg width="40" height="40" viewBox="0 0 40 40" fill="none" stroke="#fff" stroke-width="2"><circle cx="20" cy="20" r="14"/><circle cx="20" cy="20" r="6"/></svg></div><div class="cap">Complete a Comprehensive<br>Assessment, Diagnosis &amp;<br>Prognosis</div></div>
  <div class="step" style="left:356px"><span class="num" style="left:65px">2</span><div class="ring"><svg width="40" height="40" viewBox="0 0 40 40" fill="none" stroke="#fff" stroke-width="2"><rect x="12" y="6" width="18" height="22" rx="2"/><path d="M21 12v10M16 17h10M6 34h28"/></svg></div><div class="cap">Create a Treatment<br>Program</div></div>
  <div class="step" style="left:616px"><span class="num" style="left:62px">3</span><div class="ring"><svg width="40" height="40" viewBox="0 0 40 40" fill="none" stroke="#fff" stroke-width="2"><circle cx="20" cy="10" r="4"/><path d="M8 28h24M10 32h20M14 24l6-8 6 8"/></svg></div><div class="cap">Perform Your Therapy</div></div>
  <div class="step" style="left:862px"><span class="num" style="left:62px">4</span><div class="ring"><svg width="40" height="40" viewBox="0 0 40 40" fill="none" stroke="#fff" stroke-width="2"><circle cx="12" cy="10" r="3"/><path d="M12 14v16M28 6v10M24 10h8M26 26a4 4 0 1 0 0 .1"/></svg></div><div class="cap">Follow-Up Care</div></div>
  <a class="btn" style="left:537px;top:2617px;width:125px;height:42px">Quote Now</a>
</section>

<section class="testi">
  <h2>What Our Client Says</h2>
  <svg class="arrow" style="left:83px;top:210px;border:none" width="36" height="36" viewBox="0 0 36 36"><circle cx="18" cy="18" r="17" fill="none" stroke="#fff" stroke-width="1.5"/><path d="M20 12l-6 6 6 6" stroke="#fff" stroke-width="1.5" fill="none"/></svg>
  <svg class="arrow" style="left:1080px;top:210px;border:none" width="36" height="36" viewBox="0 0 36 36"><circle cx="18" cy="18" r="17" fill="none" stroke="#fff" stroke-width="1.5"/><path d="M16 12l6 6-6 6" stroke="#fff" stroke-width="1.5" fill="none"/></svg>
  <div class="card" style="left:153px">
    <div class="avatar" role="img" aria-label="Portrait of the client"></div>
    <span class="name">Dario M.</span><span class="role">Industry Specialist</span><span class="stars">★★★★★</span>
    <span class="qm" style="left:36px;top:100px">“</span>
    <p class="quote">I had a great experience with Ridgeway Roofing from start to finish. They took the time to explain in details what was wrong with my roof and gave me a very competitive estimate.</p>
    <span class="qm" style="left:160px;top:170px">”</span>
  </div>
  <div class="card" style="left:621px">
    <div class="avatar" role="img" aria-label="Portrait of the client"></div>
    <span class="name">Lena P.</span><span class="role">Specialist</span><span class="stars">★★★★★</span>
    <span class="qm" style="left:36px;top:100px">“</span>
    <p class="quote">I have been using Ridgeway Roofing over 10-15 years. They have put new roofs on 2 homes that I have owned and also siding on my family room this past year.</p>
    <span class="qm" style="left:135px;top:170px">”</span>
  </div>
</section>

<section class="blog">
  <h2 class="section-title" style="top:3190px">Our News And Blog</h2>
  <svg class="abs" style="left:83px;top:3372px" width="36" height="36" viewBox="0 0 36 36"><circle cx="18" cy="18" r="17" fill="none" stroke="#1f6e96" stroke-width="1.5"/><path d="M20 12l-6 6 6 6" stroke="#1f6e96" stroke-width="1.5" fill="none"/></svg>
  <svg class="abs" style="left:1080px;top:3372px" width="36" height="36" viewBox="0 0 36 36"><circle cx="18" cy="18" r="17" fill="none" stroke="#cfe9f3" stroke-width="1.5"/><path d="M16 12l6 6-6 6" stroke="#cfe9f3" stroke-width="1.5" fill="none"/></svg>
  <article class="post" style="left:138px">
    <div class="img" role="img" aria-label="Masked traveller reading in an airport lounge" style="background:linear-gradient(120deg,#d89a5c,#8a6b52 50%,#6e8a88)"></div>
    <span class="date">May 16 2023</span><h3>Do You Actually Need A Personal Trainer?</h3><span class="more">Read More &nbsp;→</span>
  </article>
  <article class="post" style="left:462px">
    <div class="img" role="img" aria-label="Clinicians and patients in a hospital corridor" style="background:linear-gradient(120deg,#4f6f86,#9ab0bf 50%,#3b5568)"></div>
    <span class="date">April 12 2023</span><h3>Understanding The Different Types Of Braces</h3><span class="more">Read More &nbsp;→</span>
  </article>
  <article class="post" style="left:782px">
    <div class="img" role="img" aria-label="Doctor discussing results with a patient" style="background:linear-gradient(120deg,#a8b5c2,#e4e7ea 50%,#6e8194)"></div>
    <span class="date">December 19 2022</span><h3>How To Choose The Right Pillow For Good Posture</h3><span class="more">Read More &nbsp;→</span>
  </article>
</section>

<section class="cta">
  <svg class="abs" style="left:40px;top:120px" width="120" height="130" viewBox="0 0 120 130"><circle cx="60" cy="60" r="58" fill="#47bbe0"/></svg>
  <svg class="abs" style="left:930px;top:30px" width="170" height="160" viewBox="0 0 170 160"><circle cx="85" cy="80" r="70" fill="#47bbe0"/></svg>
  <h2>Available Whenever You Need Us.</h2>
  <p>Each one of us is different and we each need a unique approach to achieve health and wellness. We offer a wide-range of evidence-based rehabilitation.</p>
  <a class="btn" style="left:538px;top:157px;width:124px;height:42px;background:#fff;color:var(--sky)">Contact Now</a>
</section>

<footer class="footer">
  <div class="brand" style="left:112px;top:40px;font-size:14px"><i style="width:30px;height:30px"></i>Quillmere Voyage Care</div>
  <div class="abs" style="left:113px;top:115px;display:flex;gap:7px">
    <i style="width:20px;height:20px;border:1.3px solid #fff;border-radius:50%"></i><i style="width:20px;height:20px;border:1.3px solid #fff;border-radius:50%"></i><i style="width:20px;height:20px;border:1.3px solid #fff;border-radius:50%"></i><i style="width:20px;height:20px;border:1.3px solid #fff;border-radius:50%"></i>
  </div>
  <span class="abs" style="left:112px;top:150px;font-size:9.5px">© 2023 Quillmere Voyage Care</span>
  <div class="fcol" style="left:311px"><h4>About</h4>About Quillmere Care<br>Our Ecosystem<br>Community Impact<br>Stories &amp; Newsroom<br>Contact Us</div>
  <div class="fcol" style="left:483px"><h4>Patient Tools</h4>Patient Portal<br>Billing &amp; Financial Services<br>Medical Records<br>All Patient Tools</div>
  <div class="fcol" style="left:656px;width:190px"><h4>Contact Us</h4>
    <div style="padding-left:26px">(866) 555-0148<br>info@quillmerevoyage.com<br>7F 12 Harbourline Tower, Meridian Avenue, Port Elsby 4410</div>
  </div>
  <div class="fcol" style="left:854px"><h4 style="font-size:16px">Subscribe To Our Newsletter</h4>
    <div style="display:flex;width:235px;height:36px;border:1px solid #fff">
      <span style="flex:1;padding:10px;font-size:8.5px;color:#c8d2e0">Enter your email</span>
      <span style="width:102px;background:#fff;color:var(--navy);font-weight:700;font-size:10px;display:flex;align-items:center;justify-content:center">Subscribe Now</span>
    </div>
  </div>
</footer>

</body>
</html>
```